Bible Word Search Activity Book Series

The design will be used across a series (3) of Word Search puzzle books on the Bibile: The Holy Bible Volume 1, The Book Of Psalms Volume 1, and the Book Of Proverbs Volume 1. The design can be the same on all three books the titles will of course just need to be different (open to creative suggestions here.) Some ideas for the titles of each include: “Bible Word Search Large Print Puzzles For Adults and Kids Volume 1,” and/or “Book Of Psalms Word Search Large Print Volume 1” etc.

Target Market(s)

Adults middle age and older and kids. The three books might also be used for a biblical word association study aid. This will be a printed book targeting those that have an interest in printed activity books and biblical study material and may want an alternative to games on electronic devices like Lumetabs.

Industry/Entity Type

Games

Font styles to use
Serif
Script

Colors

Designer to choose colors to be used in the design.

Requirements
Must have
• Most of the printed puzzle and activity books that are available today, with the exception of those published by The Harrowgate Courier are very dry would like to see something unique and eye catching with a clear title.
Nice to have
• Would be nice to perhaps have a bible somewhere in the cover design. Possible idea might be a silhouette of a person looking in to or reading the Bible. I've attached some designs from current puzzle books that have caught my attention. Design might incorporate something biblical but it doesn't necessarily have to. Would like to see the use of some color in the design.

```html
<!DOCTYPE html>
<html lang="en">
<head>
<meta charset="utf-8">
<title>Bible Word Search Large Print Puzzles – Volume 1</title>
<link href="https://fonts.googleapis.com/css2?family=Cinzel:wght@700;900&family=Raleway:wght@300;400&display=swap" rel="stylesheet">
<style>
  :root {
    --band: #7a6679;
    --page: #fbd6fb;
    --wood: #5a3a24;
    --wood-mid: #6b4529;
    --wood-dark: #3a2313;
    --gold: #c9a93a;
    --ink-light: #ffffff;
  }
  html, body { margin: 0; padding: 0; overflow: hidden; }
  .cover {
    position: relative;
    width: 848px;
    height: 1200px;
    background: var(--page);
    overflow: hidden;
    font-family: "Raleway", sans-serif;
    color: var(--ink-light);
  }
  .band {
    position: absolute;
    left: 0;
    width: 100%;
    background: var(--band);
    display: flex;
    align-items: center;
    justify-content: center;
    font-weight: 300;
    text-transform: uppercase;
    box-sizing: border-box;
  }
  .band--top { top: 0; height: 96px; font-size: 40px; letter-spacing: 0.62em; padding-left: 0.62em; }
  .band--bottom { bottom: 0; height: 104px; font-size: 35px; letter-spacing: 0.6em; padding-left: 0.6em; }
  .bouquet { position: absolute; left: 0; top: 0; width: 848px; height: 1200px; }
  .badge { position: absolute; left: 0; top: 0; width: 848px; height: 1200px; }
  .title { position: absolute; left: 0; top: 0; width: 848px; height: 1200px; margin: 0; font-weight: 400; }
  .title__line {
    position: absolute;
    left: 0;
    width: 100%;
    text-align: center;
    line-height: 1;
    white-space: nowrap;
  }
  .title__main { font-family: "Cinzel", serif; font-weight: 900; }
  .title__bible { top: 462px; font-size: 44px; letter-spacing: 0.06em; }
  .title__search { top: 514px; font-size: 44px; letter-spacing: 0.02em; }
  .title__sub { font-family: "Cinzel", serif; font-weight: 700; font-size: 40px; letter-spacing: 0.06em; }
  .title__print { top: 568px; }
  .title__puzzles { top: 622px; }
</style>
</head>
<body>
<div class="cover">
  <div class="band band--top">Volume 1</div>

  <svg class="bouquet" viewBox="0 0 848 1200" role="img" aria-label="Illustrated bouquet of pink, magenta and lavender flowers with green leaves surrounding the title">
    <defs>
      <radialGradient id="bloom" cx="50%" cy="52%" r="60%">
        <stop offset="0%" stop-color="#d9306f"/>
        <stop offset="30%" stop-color="#ea6aa0"/>
        <stop offset="55%" stop-color="#f2a3c4"/>
        <stop offset="75%" stop-color="#c7a9e0"/>
        <stop offset="100%" stop-color="#5f8a4e"/>
      </radialGradient>
    </defs>
    <path fill="url(#bloom)" d="M560 108 C600 100 640 150 660 170 C720 150 790 180 790 230 C760 250 740 270 770 320 C740 360 720 380 730 420 C760 470 740 520 780 560 C760 600 790 650 760 700 C800 740 780 790 740 810 C760 860 720 900 740 940 C720 990 700 1030 660 1050 C620 1080 560 1076 500 1070 C440 1076 380 1070 320 1030 C270 1000 240 960 220 930 C150 940 110 900 90 860 C120 820 100 780 60 740 C70 690 60 640 90 600 C60 560 80 520 130 500 C110 460 120 420 150 400 C100 380 90 330 110 300 C150 270 200 260 210 220 C240 180 300 170 330 150 C370 130 420 130 460 150 C490 120 530 110 560 108 Z"/>
  </svg>

  <svg class="badge" viewBox="0 0 848 1200" aria-hidden="true">
    <defs>
      <linearGradient id="wood" x1="0" y1="0" x2="0" y2="1">
        <stop offset="0%" stop-color="var(--wood-mid)"/>
        <stop offset="50%" stop-color="var(--wood)"/>
        <stop offset="100%" stop-color="var(--wood-dark)"/>
      </linearGradient>
    </defs>
    <path fill="url(#wood)" stroke="var(--wood-dark)" stroke-width="3"
      d="M424 358 L640 438 Q650 470 686 474 L712 568 L686 664 Q650 668 640 700 L424 780 L208 700 Q198 668 162 664 L136 568 L162 474 Q198 470 208 438 Z"/>
    <path fill="none" stroke="var(--gold)" stroke-width="3"
      d="M424 376 L628 452 Q640 482 672 488 L694 568 L672 650 Q640 656 628 686 L424 762 L220 686 Q208 656 176 650 L154 568 L176 488 Q208 482 220 452 Z"/>
  </svg>

  <h1 class="title">
    <span class="title__line title__main title__bible">BIBLE</span>
    <span class="title__line title__main title__search">WORD SEARCH</span>
    <span class="title__line title__sub title__print">LARGE PRINT</span>
    <span class="title__line title__sub title__puzzles">PUZZLES</span>
  </h1>

  <div class="band band--bottom">For Adults and Kids</div>
</div>
</body>
</html>
```